TRV Flyer

We need a professional design for flyers that we produce. The attached event draft is typical of the majority of flyers we will produce, and is the one that we need to do right now.

We would also like the source files for the design. We don’t have Corel Draw, but can work with any files produced in Adobe Creative Suite products.

Target Market(s)

Owners of residential apartments

Industry/Entity Type

Non-Profit

Requirements
Must have
• Design must be complimentary to our new website design at www.trv.org.au so we can establish consistent branding.
• Any fonts used must be freely avalaible standard fonts used in Microsoft Word

```html
<!DOCTYPE html>
<html lang="en">
<head>
<meta charset="utf-8">
<title>TRV Educational Workshop – June 2010</title>
<link href="https://fonts.googleapis.com/css2?family=Didact+Gothic&family=Jost:wght@500;600;700&display=swap" rel="stylesheet">
<style>
  :root {
    --navy: #253570;
    --teal: #3b8f9c;
    --teal-band: #3bb3c3;
    --gold: #9a8a2c;
    --ink: #141414;
    --paper: #ffffff;
  }
  * { margin: 0; padding: 0; box-sizing: border-box; }
  html, body { width: 849px; height: 1200px; overflow: hidden; background: var(--paper); }
  body { font-family: "Didact Gothic", "Century Gothic", sans-serif; color: var(--ink); font-size: 13px; }
  .flyer { position: relative; width: 849px; height: 1200px; overflow: hidden; }
  .edge { position: absolute; left: 0; width: 849px; height: 14px; background: var(--navy); }
  .edge--top { top: 0; }
  .edge--bottom { bottom: 0; }

  .brand { position: absolute; right: 45px; top: 48px; display: flex; align-items: center; gap: 8px; }
  .brand__dot { width: 14px; height: 14px; background: var(--navy); }
  .brand__name { font-family: "Jost", sans-serif; font-weight: 500; font-size: 17px; line-height: 1.05; color: var(--navy); letter-spacing: 1px; text-transform: uppercase; }

  .title-band { position: absolute; left: 0; top: 109px; width: 760px; height: 62px;
    background: linear-gradient(90deg, var(--navy) 0%, #4b5a8c 30%, #a6aec8 62%, rgba(255,255,255,0) 100%); }
  .title-band h1 { position: absolute; left: 27px; top: 9px; font-family: "Jost", sans-serif; font-weight: 600; font-size: 34px; color: #fff; letter-spacing: -0.3px; }

  .headline { position: absolute; left: 0; width: 849px; top: 182px; text-align: center; font-family: "Jost", sans-serif; font-weight: 700; }
  .headline__main { font-size: 21px; padding-left: 70px; }
  .headline__date { font-size: 17px; margin-top: 1px; padding-left: 90px; }

  .audience { position: absolute; left: 66px; top: 278px; font-size: 13px; }
  .audience p { position: absolute; white-space: nowrap; }
  .audience .arrow { position: absolute; left: 0; width: 19px; height: 10px; }
  .audience .arrow svg { display: block; }

  .details { position: absolute; left: 72px; top: 0; font-size: 13px; }
  .details .label { position: absolute; left: 0; color: var(--teal); font-weight: bold; font-family: "Jost", sans-serif; font-weight: 600; }
  .details .value { position: absolute; left: 98px; white-space: nowrap; }
  sup { font-size: 7px; }

  .note { position: absolute; left: 175px; top: 582px; }
  .register { position: absolute; left: 291px; top: 608px; color: var(--teal); }
  .register span { color: var(--ink); }

  .programme { position: absolute; left: 80px; top: 648px; width: 600px; }
  .programme h2 { font-family: "Jost", sans-serif; font-weight: 600; font-size: 15px; color: var(--teal); }
  .programme p { margin-top: 10px; line-height: 18px; }

  .sessions { position: absolute; left: 72px; top: 762px; width: 620px; border-collapse: collapse; font-size: 13px; }
  .sessions th, .sessions td { border: 1px solid #222; text-align: left; vertical-align: top; padding: 0 7px; line-height: 18px; width: 33.33%; }
  .sessions th { background: var(--teal-band); color: #fff; font-family: "Jost", sans-serif; font-weight: 600; }

  .theme { position: absolute; left: 72px; top: 913px; width: 590px; line-height: 18px; }

  .call { position: absolute; left: 120px; top: 1105px; width: 620px; font-family: "Jost", sans-serif; font-weight: 600; font-size: 13px; line-height: 18px; color: var(--gold); text-transform: uppercase; }
</style>
</head>
<body>
<main class="flyer">
  <div class="edge edge--top"></div>

  <div class="brand">
    <span class="brand__dot"></span>
    <span class="brand__name">Tower<br>Residents<br>Voice</span>
  </div>

  <header class="title-band"><h1>TRV Educational Workshop</h1></header>

  <div class="headline">
    <div class="headline__main">“The Essentials of Strata Living – What Every Owner Needs to Know”</div>
    <div class="headline__date">June 2010</div>
  </div>

  <section class="audience">
    <p style="left:22px;top:0">This workshop is for owners in strata apartments who want to learn more about</p>
    <span class="arrow" style="top:29px"><svg width="19" height="10"><polygon points="0,0 13,0 19,5 13,10 0,10 4,5" fill="#9a8a2c"/></svg></span>
    <p style="left:25px;top:25px">getting the best out of apartment living</p>
    <span class="arrow" style="top:48px"><svg width="19" height="10"><polygon points="0,0 13,0 19,5 13,10 0,10 4,5" fill="#9a8a2c"/></svg></span>
    <p style="left:25px;top:44px">protecting their home and their investment</p>
    <p style="left:22px;top:69px">AND particularly for</p>
    <span class="arrow" style="top:99px"><svg width="19" height="10"><polygon points="0,0 13,0 19,5 13,10 0,10 4,5" fill="#9a8a2c"/></svg></span>
    <p style="left:25px;top:95px">executive committee members to know their rights and responsibilities in managing their strata</p>
    <p style="left:25px;top:112px">scheme</p>
  </section>

  <section class="details">
    <span class="label" style="top:442px">Location:</span>
    <span class="value" style="top:442px">Harbourside Club</span>
    <span class="value" style="top:462px">24 Wharf Terrace</span>
    <span class="value" style="top:480px">Cove Point 2061</span>
    <span class="label" style="top:511px">Dates:</span>
    <span class="value" style="top:511px">The workshop will run twice – on 12<sup>th</sup> June and 26<sup>th</sup> June 2010</span>
    <span class="label" style="top:529px">Time:</span>
    <span class="value" style="top:529px">10.00 am to 4.00 pm.</span>
    <span class="label" style="top:547px">Cost:</span>
    <span class="value" style="top:547px">$60.00, which includes morning tea and lunch .</span>
  </section>

  <p class="note">The maximum number of participants for each workshop is 60.</p>
  <p class="register">Register at <span>www.trv.org.au</span></p>

  <section class="programme">
    <h2>Programme:</h2>
    <p>The day will comprise four sessions, each facilitated by a specialist.</p>
    <p style="margin-top:7px">In each session the speaker will provide relevant information and set the topics for group work; participants will break into groups and work up solutions to each topic; and the groups will compare outcomes.</p>
  </section>

  <table class="sessions">
    <thead><tr><th></th><th>Topic</th><th>Speaker</th></tr></thead>
    <tbody>
      <tr><td>Morning</td><td>Governance</td><td>Martin Hale, strata lawyer</td></tr>
      <tr><td></td><td>Management</td><td>Peter Lowan, seasoned former chairperson and executive committee member</td></tr>
      <tr><td>Afternoon</td><td>Financials</td><td>David Fenwick, accountant</td></tr>
      <tr><td></td><td>Physicality</td><td>Mark Severin, facilities manager</td></tr>
    </tbody>
  </table>

  <p class="theme">The day’s theme will be:<br>Gina is a new owner in her building called Utopia Tower. She notices some management processes which to her seem strange. She is elected to the executive committee and finds that the developer has retained more control than she realised - the service providers have long-term and onerous contracts, and she doesn’t seem to be able to exert enough influence. What does the law require her to do, as a committee member? How does she influence good management processes? The finances seem to be out of control, so how can she fix them so she doesn’t pay inflated levies each year and lose value on her investment? … and then the neighbour above her apartment installs a timber floor and she has noise problems … and the building seems to have a lot of defects ………….</p>

  <p class="call">Enroll now - learn a lot - have some fun as well - share experiences - find out how TRV can help you in the longer term.</p>

  <div class="edge edge--bottom"></div>
</main>
</body>
</html>
```